Gold and Ember med spa needs an awesome eye catching billboard ad

We need a billboard ad design for a Med Spa with location sin Davenport and Windermere FL A medical spa where the beauty of nature meets the power of science to treat the whole person, mind, body and soul.

Tallory Brightway Med Spa is a medical spa where the beauty of nature meets the power of science to create gorgeous, youthful looking skin. Located in Davenport, Florida, but also serving Four Corners, Celebration, and Windermere, Florida, the talented professional team brings decades of experience in world-class skin care to provide holistic, science-backed aesthetic services and health coaching.

Industry/Entity Type

Spa

Colors
fbee3e
fece3e
eea4c8
e667a6
fbee3d

Requirements
Must have
• Locations in Davenport and Dr Phillips
Phone 407-555-0193
website www.goldandemberspa-example.com

Boards for each:
Aesthetic Treatments
Cosmetic Injectables
Lumiva facial
add color vs too many earthtones, to catch the eye perhaps using yellow, something that catches the eye and stands out from the normal everyday
Thank you!!!!
Nice to have
• Boards for each:
Aesthetic Treatments
Cosmetic Injectables
Lumiva facial
add color vs too many earthtones, to catch the eye
photos that match services,
Thank you!!!!

```html
<!DOCTYPE html>
<html lang="en">
<head>
<meta charset="utf-8">
<title>Tallory Brightway Med Spa Billboard</title>
<link href="https://fonts.googleapis.com/css2?family=Baloo+2:wght@600;700;800&display=swap" rel="stylesheet">
<style>
  :root {
    --page: #eceae8;
    --board: #ffffff;
    --gold: #c9a96a;
    --ink: #2b2826;
    --yellow: #fbce3e;
    --pink: #e667a6;
    --pink-soft: #eea4c8;
    --bar: #2e2a28;
    --water: #cfe0ec;
  }
  * { box-sizing: border-box; margin: 0; padding: 0; }
  html, body { width: 1200px; height: 1200px; overflow: hidden; background: var(--page); }
  body { position: relative; font-family: "Baloo 2", sans-serif; }

  .billboard {
    position: absolute; left: 40px; top: 414px;
    width: 1120px; height: 372px;
    background: var(--board);
    border: 6px solid #f4f4f4;
    box-shadow: 0 2px 10px rgba(0,0,0,.15);
    overflow: hidden;
  }
  .water-splash {
    position: absolute; left: 0; top: 0; width: 240px; height: 100%;
    background: linear-gradient(90deg, var(--water) 0%, #e6eff5 55%, rgba(255,255,255,0) 100%);
  }
  .brand {
    position: absolute; left: 120px; top: 52px;
    color: var(--gold); font-weight: 600; line-height: 1;
  }
  .brand-mark {
    position: absolute; left: -40px; top: 6px;
    width: 26px; height: 26px; border-radius: 50%; background: var(--gold);
  }
  .brand-name { font-size: 38px; letter-spacing: 3px; white-space: nowrap; }
  .brand-sub { font-size: 20px; letter-spacing: 5px; margin-top: 8px; }
  .locations {
    font-size: 18px; letter-spacing: 1px; margin-top: 12px;
    color: var(--ink); font-weight: 600;
  }

  .phone {
    position: absolute; left: 130px; top: 200px;
    font-size: 52px; font-weight: 800; color: var(--ink); letter-spacing: 1px;
    white-space: nowrap;
  }
  .web {
    position: absolute; left: 118px; top: 272px;
    width: 420px; height: 48px; border-radius: 8px;
    background: var(--yellow); color: #fff;
    font-size: 22px; font-weight: 700; text-align: center; line-height: 52px;
    white-space: nowrap;
  }

  .service {
    position: absolute; top: 12px; height: 290px;
    display: flex; align-items: flex-end; justify-content: center;
    padding-bottom: 14px;
  }
  .service .photo {
    position: absolute; inset: 0;
    background: linear-gradient(180deg, #ece7e4 0%, #f1e2e3 55%, var(--pink-soft) 75%, var(--pink) 100%);
  }
  .service.injectables .photo {
    background: linear-gradient(180deg, #b9d8ec 0%, #d9e4ef 55%, var(--pink-soft) 75%, var(--pink) 100%);
  }
  .service .label {
    position: relative; color: #fff; font-size: 21px; font-weight: 700;
    line-height: 1.1; text-align: center; font-style: italic; white-space: nowrap;
  }
  .aesthetic { left: 590px; width: 148px; }
  .injectables { left: 746px; width: 150px; }
  .facial { left: 904px; width: 150px; }

  .social-bar {
    position: absolute; left: 1054px; top: 12px; width: 48px; height: 290px;
    background: var(--bar);
    display: flex; flex-direction: column; align-items: center; justify-content: space-evenly;
    padding: 14px 0;
  }
  .social-bar span { width: 16px; height: 16px; border-radius: 50%; background: #fff; }

  .tagline {
    position: absolute; left: 596px; top: 310px;
    font-size: 29px; font-weight: 700; color: var(--ink); font-style: italic;
    white-space: nowrap;
  }
</style>
</head>
<body>
  <div class="billboard">
    <div class="water-splash" role="img" aria-label="Splashing water droplets"></div>

    <div class="brand">
      <span class="brand-mark"></span>
      <div class="brand-name">TALLORY BRIGHTWAY</div>
      <div class="brand-sub">MED SPA</div>
      <div class="locations">Davenport &nbsp;|&nbsp; Dr Phillips</div>
    </div>

    <div class="phone">407-555-0193</div>
    <div class="web">www.goldandemberspa-example.com</div>

    <div class="service aesthetic">
      <div class="photo" role="img" aria-label="Woman receiving an aesthetic skin treatment"></div>
      <div class="label">Aesthetic<br>Treatments</div>
    </div>
    <div class="service injectables">
      <div class="photo" role="img" aria-label="Woman receiving a cosmetic injection"></div>
      <div class="label">Cosmetic<br>Injectables</div>
    </div>
    <div class="service facial">
      <div class="photo" role="img" aria-label="Woman receiving a facial treatment"></div>
      <div class="label">Lumiva Facial</div>
    </div>

    <div class="social-bar" aria-label="Social links">
      <span></span><span></span><span></span><span></span><span></span>
    </div>

    <div class="tagline">Beauty of Nature | Power of Science</div>
  </div>
</body>
</html>
```